Product labels for new supplements business targeting high performing creative people

I need a label design for different supplements like Whey, BCAA, Melatonin etc. that I could customize for each use case separately.

The brand is called lanternfolk.life, and it would be the first design of the labels. We haven't sold any products yet, but the target audience is people with growth mindset, people who want to be as efficient as possible and are constantly looking to improve their lifestyle. As part of that, they are also working out, but don't know much about supplements yet. Mostly people between 20-34.

I don't have a too specific idea of the expected design, though it should be light, warm, smart and minimalist, maybe have some patterns. It should looks smart and clean (and expensive). Orange and golden might be the additional colors for white. I have attached the templates of some products that I plan to sell and also the logo of the brand.

Here's what I have used for inspiration:
Brands that I like and are somewhat similar in concept: https://www.vimqera.com/ (!!specially the way they
bring "how the product helps them" in focus, not "what the product is" & https://www.pobri.care/ &
https://www.selvoda.com/sport/ & https://en.kambelo.fr/ &
https://gridmarket.com/profiles/corawellhaldesign/designs/417586

Here's how different products look like: https://prodaxel.com/catalog

Target Market(s)

target audience is people with growth mindset, people who want to be as efficient as possible and are constantly looking to improve their lifestyle. As part of that, they are also working out, but don't know much about supplements yet. Mostly people between 20-34.

Industry/Entity Type

Supplements

Font styles to use
Sans Serif

Colors
FFC000
F8CF3A
FAE287
FDF2CF
FEFAEE
F0912C
F2A743
F7CA91
FBE8D2
FDF5EE
EE7325
F08F49
F5BC92
FAE3D3
FDF4ED

Requirements
Must have
• Clean, smart and minimalist design that can be applied for different products in different sizes, like Whey protein, BCAA, vitamins etc. available here: https://prodaxel.com/catalog
Nice to have
• Patterns, expensive look
Should not have
• Doodles, too many colors

```html
<!DOCTYPE html>
<html lang="en">
<head>
<meta charset="UTF-8">
<title>lanternfolk.life — Beef Protein Chocolate label</title>
<link rel="stylesheet" href="https://fonts.googleapis.com/css2?family=Oswald:wght@600&family=Roboto+Condensed:wght@400&family=Roboto:wght@500&display=swap">
<style>
  :root {
    --page-bg: #f3f3f3;
    --label-yellow: #f8d43e;
    --label-yellow-light: #fae287;
    --band-orange: #f5b23a;
    --band-orange-deep: #f2a743;
    --diamond: #f7c440;
    --ink: #1c1a17;
    --ink-soft: #2b2722;
  }
  * { margin: 0; padding: 0; box-sizing: border-box; }
  html, body { width: 1200px; height: 1200px; overflow: hidden; background: var(--page-bg); }

  .label {
    position: absolute;
    left: 100px; top: 60px;
    width: 1000px; height: 1080px;
    overflow: hidden;
  }
  .label-pattern {
    position: absolute; inset: 0;
    background: radial-gradient(ellipse at 50% 45%, var(--label-yellow-light) 0%, var(--label-yellow) 70%);
  }
  .band { position: absolute; left: 0; right: 0; background: linear-gradient(90deg, var(--band-orange-deep), var(--band-orange), var(--band-orange-deep)); }
  .band-top { top: 0; height: 90px; }
  .band-bottom { top: 945px; bottom: 0; }

  .diamond {
    position: absolute;
    left: 50%; top: 540px;
    width: 580px; height: 580px;
    margin: -290px 0 0 -290px;
    background: var(--diamond);
    opacity: 0.75;
    border-radius: 48px;
    transform: rotate(45deg);
  }

  .brand {
    position: absolute; top: 280px; left: 0; right: 0;
    display: flex; justify-content: center; align-items: center; gap: 22px;
    font-family: "Roboto", sans-serif; font-weight: 500;
    font-size: 70px; color: var(--ink); letter-spacing: 0.5px;
  }
  .brand-dot { width: 56px; height: 56px; border-radius: 50%; background: #ee7325; }

  .product-name {
    position: absolute; top: 545px; left: 0; right: 0; text-align: center;
    font-family: "Oswald", sans-serif; font-weight: 600;
    font-size: 106px; line-height: 1; color: var(--ink);
    transform: scaleX(0.86); letter-spacing: -1px;
  }
  .flavour {
    position: absolute; top: 672px; left: 0; right: 0; text-align: center;
    font-family: "Roboto Condensed", sans-serif; font-size: 58px; color: var(--ink);
    letter-spacing: 1px;
  }
  .benefits {
    position: absolute; top: 762px; left: 0; right: 0; text-align: center;
    font-family: "Roboto Condensed", sans-serif; font-size: 35px; line-height: 46px;
    color: var(--ink-soft);
  }
  .benefits sup { font-size: 20px; }
  .footer-line {
    position: absolute; top: 900px; left: 66px; right: 70px;
    display: flex; justify-content: space-between;
    font-family: "Roboto Condensed", sans-serif; font-size: 34px; color: var(--ink-soft);
  }
</style>
</head>
<body>
  <main class="label">
    <div class="label-pattern" role="img" aria-label="Subtle golden scale pattern across the label"></div>
    <div class="band band-top"></div>
    <div class="band band-bottom"></div>
    <div class="diamond"></div>

    <div class="brand"><span class="brand-dot"></span><span class="brand-name">lanternfolk.life</span></div>

    <h1 class="product-name">BEEF PROTEIN</h1>
    <p class="flavour">CHOCOLATE</p>
    <p class="benefits">
      Hydrolyzed beef protein with minimum fat content<br>
      Promotes muscle gain and helps maintain muscle mass<sup>*</sup>
    </p>
    <div class="footer-line">
      <span class="supplement-type">DIETARY SUPPLEMENT</span>
      <span class="net-weight">Net Wt. 900g (31.75oz)</span>
    </div>
  </main>
</body>
</html>
```